Web Design Project

We need a web design for a new company. We have a logo, and we've identified the style of a website that we'd like to adapt (www.torvelmint.com). We do not sell to the public. The purpose of the site is (1) to allow our appointed sales partners to log in to our proprietary database system and (2) to provide a basic web presence and some basic information about our company.

We sell business insurance through independent agents - our sales partners.

Please do not use a photo of a person/s as a central design element, or at all.

Target Market(s)

The purpose of the site is not to sell, but to provide a professional landing page for a log in and some basic company information.

Industry/Entity Type

Business

Requirements
Must have
• A professional look. Agent log in must be central, clear and easy. Use of our logo and our colors.
Should not have
• Photos of people

```html
<!DOCTYPE html>
<html lang="en">
<head>
<meta charset="utf-8">
<title>Harbor Crest Insurance</title>
<link href="https://fonts.googleapis.com/css2?family=PT+Sans+Narrow:wght@400;700&family=PT+Sans:wght@400;700&family=Ubuntu:wght@400&display=swap" rel="stylesheet">
<style>
:root{
  --navy-deep:#0b1c26;
  --hero-top:#1d4a64;
  --hero-mid:#24607f;
  --sky:#3cb8e4;
  --sky-soft:#4fa9d6;
  --white:#ffffff;
  --text:#4a4f55;
  --text-soft:#6a7076;
  --heading:#3c4046;
  --rule:#cfd3d6;
  --strip:#ececec;
  --bullet:#4fa9d6;
}
*{margin:0;padding:0;box-sizing:border-box}
html,body{width:1200px;height:866px;overflow:hidden;background:var(--white)}
body{position:relative;font-family:"PT Sans Narrow",sans-serif;color:var(--text)}
.abs{position:absolute}

.hero{left:0;top:0;width:1200px;height:400px;
  background:linear-gradient(180deg,var(--hero-top) 0%,var(--hero-mid) 60%,#2f7ca1 100%)}
.topbar{left:0;top:24px;width:1200px;height:61px;
  background:repeating-linear-gradient(135deg,#0f2532 0 2px,#142d3c 2px 4px)}
.brand{left:197px;top:7px;width:100px;height:117px;background:var(--navy-deep);border-radius:6px;
  display:flex;flex-direction:column;align-items:center;justify-content:center;gap:8px}
.brand-mark{width:14px;height:14px;background:var(--white)}
.brand-name{font-family:"PT Sans Narrow",sans-serif;font-weight:700;color:var(--white);font-size:14px;
  text-align:center;line-height:1.1;text-transform:uppercase}
.nav{right:170px;top:47px;display:flex;gap:39px;list-style:none}
.nav li{font-family:"PT Sans Narrow",sans-serif;font-weight:700;font-size:12.5px;letter-spacing:.5px;
  text-transform:uppercase;color:var(--sky)}
.nav li.active{color:var(--white)}

.skyline{left:178px;top:130px;width:440px;height:270px;
  background:radial-gradient(ellipse at 50% 55%,#10283a 0%,#163b52 45%,rgba(36,96,127,0) 75%)}

.hero-title{left:666px;top:124px;font-family:"Ubuntu",sans-serif;font-weight:400;font-size:30px;line-height:36px;color:var(--white);white-space:nowrap}
.hero-title .accent{color:var(--sky)}
.hero-sub{left:666px;top:205px;font-family:"Ubuntu",sans-serif;font-size:16px;color:var(--sky);white-space:nowrap}
.hero-rule{left:666px;top:235px;width:354px;border-top:2px dotted rgba(60,184,228,.55)}
.hero-copy{left:666px;top:246px;width:354px;font-size:12.5px;line-height:19px;color:var(--white)}
.btn-primary{left:667px;top:320px;width:84px;height:34px;background:var(--sky);color:var(--white);
  font-size:13px;display:flex;align-items:center;justify-content:center}

.strip{left:0;top:400px;width:1200px;height:25px;background:var(--strip);border-bottom:1px solid #dcdcdc}

.card-head{top:447px;width:238px;height:31px;background:var(--navy-deep);color:var(--white);
  font-family:"PT Sans",sans-serif;font-weight:700;font-size:15px;display:flex;align-items:center;justify-content:center}
.card-photo{top:483px;width:238px;height:122px}
.photo-city{background:linear-gradient(180deg,#8fa6b8 0%,#5f7280 50%,#4e6a3e 100%)}
.photo-tower{background:linear-gradient(180deg,#4a86c8 0%,#9ec3e6 50%,#d6e4ee 100%)}
.photo-sculpture{background:linear-gradient(90deg,#141a4a 0%,#b3301a 45%,#d84a1c 65%,#1a1f5e 100%)}
.card-title{top:619px;width:238px;height:33px;border-top:1px solid var(--rule);border-bottom:1px solid var(--rule);
  font-family:"PT Sans",sans-serif;font-weight:400;font-size:16.5px;line-height:31px;color:var(--heading);
  letter-spacing:.2px;white-space:nowrap}
.card-title .link{color:var(--sky-soft)}

.products{left:197px;top:661px;list-style:none}
.products li{font-size:12.5px;letter-spacing:.6px;color:var(--text-soft);height:21px;padding-left:19px;position:relative}
.products li::before{content:"";position:absolute;left:2px;top:7px;width:5px;height:5px;border-radius:50%;background:var(--bullet)}
.link-arrow{font-size:12.5px;color:var(--sky-soft);display:flex;align-items:center;gap:6px}

.claim-label{font-size:12.5px;color:var(--text-soft);white-space:nowrap}
.claim-col{top:686px;width:76px;text-align:center}
.claim-btn{top:708px;height:31px;background:linear-gradient(#fafafa,#e4e6e8);border:1px solid #cfd3d6;
  color:var(--sky-soft);font-size:11.5px;display:flex;align-items:center;justify-content:center;white-space:nowrap}

.field{left:766px;width:238px;height:28px;border:1px solid #c9cdd0;display:flex}
.field-label{width:56px;border-right:1px solid #c9cdd0;font-size:11.5px;letter-spacing:.5px;color:var(--text-soft);
  display:flex;align-items:center;justify-content:center}
.btn-submit{left:766px;top:741px;width:88px;height:30px;background:linear-gradient(#fafafa,#e1e3e5);border:1px solid #cfd3d6;
  color:var(--sky-soft);font-family:"PT Sans",sans-serif;font-size:12.5px;letter-spacing:.5px;display:flex;align-items:center;justify-content:center}

.footer{left:0;top:811px;width:1200px;height:55px;
  background:repeating-linear-gradient(135deg,#383b3e 0 2px,#414447 2px 4px);border-top:5px solid #2c2e30}
.copyright{left:170px;top:831px;font-size:12.5px;color:var(--white)}
.copyright .link{color:var(--sky-soft)}
.footer-nav{right:170px;top:831px;display:flex;gap:32px;list-style:none;font-size:12.5px;color:var(--white)}
.footer-nav .link{color:var(--sky-soft)}
</style>
</head>
<body>

<section class="abs hero" aria-label="Welcome"></section>
<div class="abs skyline" role="img" aria-label="City skyline silhouette reflected on water"></div>
<div class="abs topbar"></div>
<div class="abs brand"><span class="brand-mark"></span><span class="brand-name">Harbor Crest<br>Insurance</span></div>
<ul class="abs nav">
  <li class="active">Home</li><li>About Us</li><li>Insurance Products</li><li>Our Team</li><li>Contact Us</li>
</ul>

<h1 class="abs hero-title"><span class="accent">Sungelle Molestielle</span><br>Fore Refed Berreferid</h1>
<p class="abs hero-sub">Proin vehicula pulvinar nisi ac semper</p>
<div class="abs hero-rule"></div>
<p class="abs hero-copy">Lorem ipsum dolor sit amet, consectetur adipiscing elit. Praesent dolor nunc, rhoncus porttitor bibendum in, placerat sed dui rae-sent suscipit consequat nunc, et accumsan arcu.</p>
<div class="abs btn-primary">read more</div>

<div class="abs strip"></div>

<!-- Products -->
<h2 class="abs card-head" style="left:197px">Our Products</h2>
<div class="abs card-photo photo-city" style="left:197px" role="img" aria-label="Aerial view of a river city with bridges"></div>
<h3 class="abs card-title" style="left:197px">Insurance Products</h3>
<ul class="abs products">
  <li>Commercial Package</li><li>Commercial Auto</li><li>Workers Compensation</li><li>Commercial Umbrella</li>
</ul>
<div class="abs link-arrow" style="left:198px;top:760px">read more
  <svg width="13" height="8" viewBox="0 0 13 8"><path d="M0 4H11M8 1l3 3-3 3" fill="none" stroke="#4fa9d6" stroke-width="1.3"/></svg></div>

<!-- Policyholder -->
<h2 class="abs card-head" style="left:484px">Policyholder Login</h2>
<div class="abs card-photo photo-tower" style="left:484px" role="img" aria-label="Modern glass office tower against blue sky"></div>
<h3 class="abs card-title" style="left:484px">Make Payments <span class="link">Report Claims</span></h3>
<p class="abs claim-label" style="left:483px;top:661px">Report a claim:</p>
<p class="abs claim-label claim-col" style="left:484px">Contact Agent</p>
<p class="abs claim-label claim-col" style="left:564px">Emergency</p>
<p class="abs claim-label claim-col" style="left:645px">Auto Glass</p>
<div class="abs claim-btn" style="left:484px;width:76px">click here</div>
<div class="abs claim-btn" style="left:564px;width:76px">(800) 555 0142</div>
<div class="abs claim-btn" style="left:645px;width:77px">(800) 555 0142</div>
<div class="abs claim-label" style="left:485px;top:760px;display:flex;gap:12px">Make a Payment Online:
  <span class="link-arrow">Click Here
  <svg width="13" height="8" viewBox="0 0 13 8"><path d="M0 4H11M8 1l3 3-3 3" fill="none" stroke="#4fa9d6" stroke-width="1.3"/></svg></span></div>

<!-- Agents -->
<h2 class="abs card-head" style="left:766px">Agents Staff Login</h2>
<div class="abs card-photo photo-sculpture" style="left:766px" role="img" aria-label="Red steel sculpture lit at night in a plaza"></div>
<h3 class="abs card-title" style="left:766px">Agency Services</h3>
<div class="abs field" style="top:663px"><span class="field-label">Name</span></div>
<div class="abs field" style="top:700px"><span class="field-label">Password</span></div>
<div class="abs btn-submit">Submit</div>

<footer class="abs footer"></footer>
<p class="abs copyright">Copyright © 2012 <span class="link">stonefern</span> design &nbsp;|&nbsp; All rights reserved</p>
<ul class="abs footer-nav"><li>Home</li><li>About</li><li>Contact</li><li class="link">Login</li></ul>

</body>
</html>
```